Lorvika.no is a new website about pedagogical entrepreneurship. It's main target group is teachers. The Fjellmark Institute for Classroom Media and the Nordvik Agency for Schools and Study are leading the project.

The web page is meant to show examples of how different methods of entrepreneurship can be used pedagogical in a learning environment. The page will also support the user with examples of different teaching programs and other examples of best practice.

Pedagogical entrepreneurship is not about business and men in suits. It's a method for learning. The focus in the design should be on school, education and new ways of learning.

The final product should be motivating and engaging, but at the same time governmental and serious. We are not looking for something "flashy" and corporate-looking, but a moderate, task-focused and clean design that state quality.

We need designs for three pages:
1 - frontpage
2 - subpage ("Metoder og undervisningsopplegg")
3 - subpage ("Smått-VERK i Brekkelia")

The interaction design for these three pages will be uploaded as an attachment.

We would like you to find inspiration in the following websites:
- www.gryvekst.no
- www.lavrek.no
- www.tovandstudio.com
- www.kvp.no
(more will be added)

Please use the attached logo, and feel free to use this as an inspiration for the rest of the design.

Target Market(s)

Teachers

Industry/Entity Type

Education

Requirements
Must have
• * Header with: Logo. Main navigation. Utility navigation. Search box.
* Footer
Should not have
• Images of men in suits.
Very strong graphical elements that stands out too much (we want it clean).

```html
<!DOCTYPE html>
<html lang="en">
<head>
<meta charset="utf-8">
<title>Lorvika.no – Smått-Verk at Brekkelia School</title>
<link href="https://fonts.googleapis.com/css2?family=Ubuntu:wght@400;500;700&family=Arimo:wght@400;700&display=swap" rel="stylesheet">
<style>
:root{
  --page-bg:#d3e5f0;
  --card:#ffffff;
  --blue:#2b79b5;
  --blue-dark:#2a6d9e;
  --link:#3a8fcf;
  --ink:#222;
  --panel:#f4f4f4;
  --line:#dcdcdc;
  --footer:#222222;
  --footer-text:#f0f0f0;
}
*{box-sizing:border-box;margin:0;padding:0}
html,body{width:1094px;height:1200px;overflow:hidden}
body{background:linear-gradient(180deg,#d9e9f3,#cfe1ec);font-family:Arimo,Arial,sans-serif;color:var(--ink);position:relative}
.site{position:absolute;left:29px;top:10px;width:1035px;height:1179px;background:var(--card);border-radius:8px;overflow:hidden}
.abs{position:absolute}
.utility{top:11px;left:581px;font-family:Ubuntu,sans-serif;font-size:13px}
.utility a{color:var(--blue-dark);text-decoration:none;position:absolute;white-space:nowrap}
.brand{left:43px;top:44px;display:flex;align-items:center;gap:10px}
.brand-dot{width:34px;height:34px;border-radius:50%;background:var(--blue)}
.brand-name{font-family:Ubuntu,sans-serif;font-weight:500;font-size:30px;color:var(--blue)}
.search{left:787px;top:46px;width:207px;height:29px;border:1px solid #aab;border-radius:3px;background:#fff;overflow:hidden}
.search-btn{position:absolute;right:0;top:0;width:37px;height:27px;background:linear-gradient(#3b86c6,#1f5f99);display:flex;align-items:center;justify-content:center}
.band{left:41px;top:98px;width:953px;height:95px;background:linear-gradient(180deg,#63b8e6 0%,#3e93c9 55%,#286d9f 100%)}
.band-title{position:absolute;left:0;right:0;top:64px;text-align:center;color:#fff;font-family:Ubuntu,sans-serif;font-weight:500;font-size:18px}
.mainnav{left:254px;top:98px;width:522px;height:55px;background:#fff;border-radius:0 0 6px 6px;box-shadow:0 2px 4px rgba(0,0,0,.3);display:flex;align-items:center;padding-left:14px}
.navitem{display:flex;align-items:center;gap:8px;font-family:Ubuntu,sans-serif;font-size:12px;line-height:15px;color:#222;font-weight:500;padding-right:14px;margin-right:14px;border-right:1px solid #bbb}
.navitem:last-child{border:0;color:var(--link);font-size:13px;font-weight:700;margin:0}
.content{left:41px;top:193px;width:953px;height:708px;background:var(--panel)}
.box{background:#fff;border:1px solid var(--line)}
.intro{left:82px;top:217px;width:874px;height:290px}
.intro h1{position:absolute;left:17px;top:17px;font-family:Ubuntu,sans-serif;font-size:16px;font-weight:500;color:var(--blue-dark)}
.lead{position:absolute;left:17px;top:47px;width:450px;font-size:12px;font-weight:700;line-height:15px}
.body{font-size:11px;line-height:14px;color:#333}
.intro .body{position:absolute;left:17px;top:87px;width:435px}
.fact{position:absolute;display:flex;gap:12px;font-size:11px;line-height:15px}
.fact b{display:block;color:#333}
.fact span,.fact u{color:#555}
.side-card{background:#f2f2f2;border:1px solid var(--line)}
.school{left:730px;top:244px;width:208px;height:171px}
.school-head{position:absolute;left:44px;top:11px;font-size:12px;line-height:14px}
.school-head b{color:#444}
.photo{position:absolute;left:9px;top:53px;width:189px;height:108px;background:linear-gradient(180deg,#c9d3de 0%,#8d8a7e 45%,#b66b52 65%,#e6e9ee 100%)}
.contact{left:730px;top:424px;width:208px;height:64px}
.avatar{position:absolute;left:7px;top:9px;width:30px;height:44px;border-radius:15px;background:linear-gradient(#d89a4e,#e8e8ec)}
.story{left:83px;top:531px;width:521px;height:342px;padding:17px 48px 17px 19px}
.story h2{font-size:12px;font-weight:700;margin-bottom:2px;margin-top:12px}
.story h2:first-child{margin-top:0}
.story .gap{margin-top:14px}
.media{left:630px;top:531px;width:324px;height:342px;background:#d9d9d9;border:1px solid #ccc}
.media-label{position:absolute;left:18px;top:13px;font-size:11px;color:#444}
.tabs{position:absolute;left:18px;top:36px;display:flex}
.tab{height:27px;padding:7px 11px;font-size:11px;font-weight:700;background:#f0f0f0;border:1px solid #ccc;border-bottom:0}
.tab.active{background:#fff}
.media-panel{position:absolute;left:18px;top:63px;width:287px;height:250px;background:#fff}
.video{position:absolute;left:12px;top:17px;width:260px;height:144px;background:linear-gradient(180deg,#9fb1a9 0%,#4f6463 45%,#1f3640 70%,#0f1c22 100%)}
.vbar{position:absolute;left:0;right:0;bottom:0;height:16px;background:rgba(0,0,0,.55)}
.vlink{position:absolute;left:12px;top:180px;font-size:11px;font-weight:700;color:#444;text-decoration:underline}
.vtext{position:absolute;left:12px;top:198px;font-size:11px;color:#555}
.footer{left:0;top:939px;width:1035px;height:190px;background:var(--footer)}
.footer-name{position:absolute;left:52px;top:70px;font-family:Ubuntu,sans-serif;font-weight:500;font-size:22px;color:var(--link)}
.fcol{position:absolute;top:30px;font-family:Ubuntu,sans-serif;color:var(--footer-text);font-size:14px}
.fcol h3{color:var(--link);font-size:18px;font-weight:500;margin-bottom:5px}
.fcol li{list-style:none;line-height:24px}
.fcol li.more{text-decoration:underline}
.about{left:0;top:1129px;width:1035px;height:50px;background:linear-gradient(#3a3a3a,#1a1a1a);text-align:center;line-height:44px;font-family:Ubuntu,sans-serif;font-weight:500;font-size:17px;color:#fff}
.about span{color:var(--link)}
</style>
</head>
<body>
<div class="site">
  <nav class="abs utility">
    <a style="left:0;top:0">Best Practice School</a>
    <a style="left:169px;top:0">Lorvimeter</a>
    <a style="left:303px;top:0">About lorvika.no</a>
  </nav>
  <div class="abs brand"><span class="brand-dot"></span><span class="brand-name">Lorvika</span></div>
  <div class="abs search">
    <div class="search-btn"><svg width="14" height="14" viewBox="0 0 14 14"><circle cx="8" cy="6" r="4" fill="none" stroke="#fff" stroke-width="2"/><line x1="5" y1="9" x2="1" y2="13" stroke="#fff" stroke-width="2.4"/></svg></div>
  </div>

  <header class="abs band"><div class="band-title">Smått-Verk at Brekkelia School</div></header>
  <nav class="abs mainnav">
    <div class="navitem"><svg width="28" height="24" viewBox="0 0 28 24"><path d="M14 5C10 2 5 2 2 3v17c3-1 8-1 12 2 4-3 9-3 12-2V3c-3-1-8-1-12 2z" fill="none" stroke="#222" stroke-width="2" stroke-linejoin="round"/><line x1="14" y1="5" x2="14" y2="22" stroke="#222" stroke-width="2"/></svg>What is pedagogical<br>enterpreneurship ?</div>
    <div class="navitem"><svg width="30" height="30" viewBox="0 0 30 30"><circle cx="15" cy="15" r="9" fill="none" stroke="#111" stroke-width="5" stroke-dasharray="4 3"/><circle cx="15" cy="15" r="7" fill="none" stroke="#111" stroke-width="3"/></svg>Method and<br>teaching plans</div>
    <div class="navitem"><svg width="30" height="30" viewBox="0 0 30 30"><path d="M4 9h7a3 3 0 1 1 6 0h7v7a3 3 0 1 0 0 6v6H4z" fill="#3a8fcf"/></svg>Good Example/<br>Best Practice</div>
  </nav>

  <main class="abs content"></main>

  <section class="abs box intro">
    <h1>Smått-VERK i Brekkelia</h1>
    <p class="lead">Lorem ipsum dolor sit amet, consectetur adipisicing elit, sed do eiusmod tempor incididunt ut labore et dolore magna aliqua.</p>
    <p class="body">Ut enim ad minim veniam, quis nostrud exercitation ullamco laboris nisi ut aliquip ex ea commodo consequat. Duis aute irure dolor in reprehenderit in voluptate velit esse cillum dolore eu fugiat nulla pariatur. Excepteur sint occaecat cupidatat non proident, sunt in culpa qui officia deserunt mollit anim id est laborum.</p>
    <div class="fact" style="left:19px;top:176px"><svg width="24" height="24" viewBox="0 0 24 24"><circle cx="12" cy="12" r="10" fill="#cfe3f3" stroke="#8ab" stroke-width="1.5"/><path d="M12 6v6l4 2" stroke="#567" stroke-width="1.5" fill="none"/></svg><div><b>Time spent</b><span>Text</span></div></div>
    <div class="fact" style="left:19px;top:223px"><svg width="22" height="22" viewBox="0 0 22 22"><rect x="1" y="1" width="20" height="20" fill="#c8642e"/><circle cx="13" cy="13" r="6" fill="#e8c23a"/></svg><div><b>Method</b><u>VERK</u></div></div>
    <div class="fact" style="left:209px;top:223px"><svg width="22" height="24" viewBox="0 0 22 24"><rect x="1" y="2" width="20" height="21" fill="#f2f2f2" stroke="#bbb"/><rect x="1" y="2" width="20" height="5" fill="#4caf50"/></svg><div><b>Subject</b><span>English, Norwegian, Maths</span></div></div>
  </section>

  <aside class="abs side-card school">
    <svg class="abs" style="left:10px;top:10px" width="24" height="26" viewBox="0 0 24 26"><path d="M2 12L12 3l10 9v13H2z" fill="#e05b4a"/><rect x="6" y="15" width="4" height="4" fill="#fff"/><rect x="14" y="15" width="4" height="4" fill="#fff"/></svg>
    <div class="school-head"><b>Brekkelia skole</b><br><span style="font-size:11px;color:#555">4th grade</span></div>
    <div class="photo" role="img" aria-label="Photo of the school building with a bare tree and snowy schoolyard"></div>
  </aside>
  <aside class="abs side-card contact">
    <div class="avatar" role="img" aria-label="Contact person avatar"></div>
    <div class="fact" style="left:44px;top:15px"><div><b>Contact</b><span>John Doe</span></div></div>
  </aside>

  <article class="abs box story body">
    <h2>This is how we did it</h2>
    <p>Ut enim ad minim veniam, quis nostrud exercitation ullamco laboris nisi ut aliquip ex ea commodo consequat. Duis aute irure dolor in reprehenderit in voluptate velit esse cillum dolore eu fugiat nulla pariatur. Excepteur sint occaecat cupidatat non proident, sunt in culpa qui officia deserunt mollit anim id est laborum.</p>
    <h2>Title</h2>
    <p>Ut enim ad minim veniam, quis nostrud exercitation ullamco laboris nisi ut aliquip ex ea commodo consequat. Duis aute irure dolor in reprehenderit in voluptate velit esse cillum dolore eu fugiat nulla pariatur. Excepteur sint occaecat cupidatat non proident, sunt in culpa qui officia deserunt mollit anim id est laborum.</p>
    <p class="gap">Ut enim ad minim veniam, quis nostrud exercitation ullamco laboris nisi ut aliquip ex ea commodo consequat. Duis aute irure dolor in reprehenderit in voluptate velit esse cillum dolore eu fugiat nulla pariatur. Excepteur sint occaecat cupidatat non proident, sunt in culpa qui officia deserunt mollit anim id est laborum.</p>
    <h2>Title</h2>
    <p>Ut enim ad minim veniam, quis nostrud exercitation ullamco laboris nisi ut aliquip ex ea commodo consequat. Duis aute irure dolor in reprehenderit in voluptate velit esse cillum dolore eu fugiat nulla pariatur. Excepteur sint occaecat cupidatat non proident, sunt in culpa qui officia deserunt mollit anim id est laborum.</p>
  </article>

  <section class="abs media">
    <div class="media-label">Multimedia</div>
    <div class="tabs"><div class="tab active">Videos (1)</div><div class="tab">Images (4)</div></div>
    <div class="media-panel">
      <div class="video" role="img" aria-label="Video still of a stormy sea under a grey sky">
        <div class="vbar"><svg width="14" height="16" viewBox="0 0 14 16"><path d="M5 4l5 4-5 4z" fill="#fff"/></svg></div>
      </div>
      <div class="vlink">See video</div>
      <div class="vtext">Short text about the video</div>
    </div>
  </section>

  <footer class="abs footer">
    <div class="footer-name">Lorvika</div>
    <div class="fcol" style="left:156px"><h3>Pedagonal Enterpreneurship</h3><ul><li>What is pedagonal enterpreneurship?</li><li>Science</li><li>Best practice schools</li><li>Lorvimeter</li></ul></div>
    <div class="fcol" style="left:454px"><h3>Methods</h3><ul><li>Story line</li><li>VERK</li><li>Cafe-pedagoikk</li><li class="more">See more...</li></ul></div>
    <div class="fcol" style="left:609px"><h3>Teaching Plans</h3><ul><li>1st Project Learning</li><li>Forest Tour</li><li>Startup Company</li><li class="more">See more...</li></ul></div>
    <div class="fcol" style="left:797px"><h3>Gode Eksampler</h3><ul><li>Smått-Verk at Brekkelia School</li><li>Smått-Verk at Brekkelia School</li><li>Smått-Verk at Brekkelia School</li><li class="more">See more...</li></ul></div>
  </footer>
  <div class="abs about">About <span>Lorvika.no</span></div>
</div>
</body>
</html>
```